Fresh Tarrow Work Post - Business Card Required

Dear All,

I own Velmira Limited, which in turn owns the website:
www.harbinworkpost.example

I want all of you wonderful creative people to come up with a slick, and awesome business card design that incorporates the logo on the site, and some colouring and design elements from it.

You have free reign in how you go about doing this, I won't be giving my contact details on this platform, but the winner will be asked to redesign based on my contact details which I will supply at the end.

I need the design to be completed within 5 days. I need the final print copies of the business cards by the 25th November, so unfortunately it's a bit of a rush to get these designs ready.

Any questions, please ask.

Thank you
Updates

Thank you all for your hard work and exceptional designs provided. I do have to pick one, so I have a very clear idea of which one this is, however I will wait one further day until the competition closes to be fair to all those have submitted, or are in the process of submitting. I wish you all the best and thank you again for your dedication.

```html
<!DOCTYPE html>
<html lang="en">
<head>
<meta charset="utf-8">
<title>Fresh Tarrow Work Post – Business Card</title>
<link rel="stylesheet" href="https://fonts.googleapis.com/css2?family=Questrial&display=swap">
<style>
  :root {
    --stage: #4a4a4a;
    --stage-light: #6a6a6a;
    --card-white: #ffffff;
    --ink-brown: #8a5412;
    --ink-dark: #6b3f0c;
    --gold-deep: #b7791f;
    --gold-mid: #d9a441;
    --gold-light: #f6e6a6;
    --sand-edge: #dcc09b;
    --sand-light: #f1e5d4;
    --band-gold: #d39a3a;
  }
  * { margin: 0; padding: 0; box-sizing: border-box; }
  html, body { width: 1200px; height: 800px; overflow: hidden; }
  body {
    background: radial-gradient(ellipse at 50% 45%, var(--stage-light) 0%, var(--stage) 70%);
    font-family: "Questrial", "Century Gothic", sans-serif;
    position: relative;
  }
  .card {
    position: absolute;
    left: 309px;
    width: 581px;
    height: 314px;
    border-radius: 12px;
    overflow: hidden;
    box-shadow: 0 4px 10px rgba(0,0,0,0.45);
  }
  .card-front { top: 64px; background: var(--card-white); }
  .card-back {
    top: 415px;
    height: 315px;
    background: var(--sand-edge);
  }
  .front-sweep { position: absolute; inset: 0; }
  .contact-block {
    position: absolute;
    left: 82px;
    top: 70px;
    color: var(--ink-brown);
  }
  .person-name { font-size: 26px; line-height: 1; margin-left: 24px; }
  .person-title { font-size: 15px; margin: 6px 0 0 24px; }
  .contact-list { list-style: none; margin-top: 14px; }
  .contact-list li {
    display: flex;
    align-items: flex-start;
    font-size: 15px;
    line-height: 18px;
    margin-bottom: 8px;
  }
  .contact-list svg { width: 14px; height: 16px; margin: 1px 10px 0 0; flex: none; fill: var(--ink-dark); }
  .front-brand {
    position: absolute;
    left: 398px;
    top: 100px;
    width: 130px;
    text-align: center;
    color: var(--gold-deep);
  }
  .brand-dot {
    display: block;
    width: 14px; height: 14px;
    border-radius: 50%;
    background: var(--gold-mid);
    margin: 0 auto 6px;
  }
  .front-brand .brand-name { font-size: 13px; letter-spacing: 1px; line-height: 1.2; }
  .back-glow { position: absolute; inset: 0; }
  .back-brand {
    position: absolute;
    left: 0; right: 0;
    top: 110px;
    text-align: center;
    color: var(--gold-deep);
  }
  .back-brand .brand-dot { width: 28px; height: 28px; margin-bottom: 16px; }
  .back-brand .brand-name { font-size: 22px; letter-spacing: 3px; }
  .back-band {
    position: absolute;
    left: 0; right: 0; bottom: 0;
    height: 28px;
    background: linear-gradient(90deg, var(--band-gold), #c1862a 50%, var(--band-gold));
    color: #fff;
    font-size: 15px;
    letter-spacing: 1px;
    text-align: center;
    line-height: 28px;
  }
</style>
</head>
<body>

<section class="card card-front">
  <svg class="front-sweep" viewBox="0 0 581 314" aria-hidden="true">
    <defs>
      <linearGradient id="goldSweep" x1="0" y1="1" x2="1" y2="0">
        <stop offset="0" stop-color="#c98a2b"/>
        <stop offset="0.45" stop-color="#f6e6a6"/>
        <stop offset="0.7" stop-color="#a8641a"/>
        <stop offset="1" stop-color="#f3dc8e"/>
      </linearGradient>
    </defs>
    <path d="M270 314 C400 300 540 260 581 170 L581 314 Z" fill="url(#goldSweep)"/>
    <path d="M300 312 C420 296 545 250 581 178" fill="none" stroke="#ffffff" stroke-width="3"/>
  </svg>

  <div class="contact-block">
    <h1 class="person-name">Tomas Reyl</h1>
    <p class="person-title">Managing Director</p>
    <ul class="contact-list">
      <li>
        <svg viewBox="0 0 14 16"><path d="M7 0a5 5 0 0 0-5 5c0 4 5 11 5 11s5-7 5-11a5 5 0 0 0-5-5zm0 7a2 2 0 1 1 0-4 2 2 0 0 1 0 4z"/></svg>
        <span>12 Carrow Lane, Eastfield,<br>Tarrow, TR4 9QL</span>
      </li>
      <li>
        <svg viewBox="0 0 14 16"><path d="M4 0h6a1.5 1.5 0 0 1 1.5 1.5v13A1.5 1.5 0 0 1 10 16H4a1.5 1.5 0 0 1-1.5-1.5v-13A1.5 1.5 0 0 1 4 0zm0 2v11h6V2z"/></svg>
        <span>0700 555 0142</span>
      </li>
      <li>
        <svg viewBox="0 0 14 16"><path d="M0 4h14v9H0zm1 1l6 4 6-4z"/></svg>
        <span>contact@harbinworkpost.example</span>
      </li>
      <li>
        <svg viewBox="0 0 14 16"><circle cx="7" cy="8" r="6.5"/><path d="M7 1.5v13M0.5 8h13" stroke="#fff" stroke-width="1"/></svg>
        <span>www.harbinworkpost.example</span>
      </li>
    </ul>
  </div>

  <div class="front-brand">
    <span class="brand-dot"></span>
    <p class="brand-name">FRESH TARROW<br>WORK POST</p>
  </div>
</section>

<section class="card card-back">
  <svg class="back-glow" viewBox="0 0 581 315" aria-hidden="true">
    <defs>
      <radialGradient id="sandGlow" cx="0.5" cy="0.45" r="0.6">
        <stop offset="0" stop-color="#f4ebde"/>
        <stop offset="1" stop-color="#ead8bf"/>
      </radialGradient>
    </defs>
    <ellipse cx="290" cy="330" rx="300" ry="340" fill="url(#sandGlow)"/>
  </svg>
  <div class="back-brand">
    <span class="brand-dot"></span>
    <p class="brand-name">FRESH TARROW WORK POST</p>
  </div>
  <div class="back-band">www.harbinworkpost.example</div>
</section>

</body>
</html>
```